BAYSIDE SUDS LAUNDROMAT

I NEED A SIGN FOR A NEW LAUNDROMAT THAT I HAVE BUILT
IN THE CITY OF DARWIN BESIDE MY CURRENT HOTEL I OWN
THIS IS A SEMI STAND ALONE BUSNIESS
DARWIN IS A LAID BACK CITY IN AUSTRALIA WERE THING ARE A BIT CHEEKY THE SIGN /LOGO ECT WILL BE APPRO 2 METERS TALL BY 6 METERS LONG ,6 FOOT BY 18 FOOT
sign viewing point is 5 meters to 100 meters

i have put a logo up of my current hotel as a guide it docent have to mach it just food for thought idea

building colour is white and black

like it to be fun or a little sexy risky

```html
<!DOCTYPE html>
<html lang="en">
<head>
<meta charset="utf-8">
<title>Laundromat Sign</title>
<link href="https://fonts.googleapis.com/css2?family=Bebas+Neue&family=Oswald:wght@600&family=Playball&display=swap" rel="stylesheet">
<style>
  :root {
    --page-bg: #eef1f4;
    --sign-frame: #f4f5f2;
    --navy-deep: #0b1d4a;
    --navy-mid: #1a3a7c;
    --headline: #f3f1ea;
    --script: #f2f2f2;
    --phone: #f2b21c;
    --badge-ring: #c8202a;
    --badge-fill: #e9e9e6;
  }
  * { box-sizing: border-box; margin: 0; padding: 0; }
  html, body {
    width: 1200px; height: 1200px; overflow: hidden;
    background: var(--page-bg);
  }
  .sign {
    position: absolute;
    left: 50px; top: 410px;
    width: 1100px; height: 380px;
    border: 14px solid var(--sign-frame);
    box-shadow: 0 6px 18px rgba(0,0,0,0.18);
    background: linear-gradient(180deg, var(--navy-deep) 0%, var(--navy-mid) 55%, var(--navy-deep) 100%);
    overflow: hidden;
  }
  .sign__mascot {
    position: absolute;
    left: -6px; top: 130px;
    width: 270px; height: 270px;
    border-radius: 50%;
    border: 5px solid var(--badge-ring);
    background: radial-gradient(circle at 45% 45%, #ffffff 0%, var(--badge-fill) 70%, #cfcfcc 100%);
  }
  .sign__headline {
    position: absolute;
    left: 36px; top: 40px;
    font-family: 'Bebas Neue', sans-serif;
    font-size: 150px;
    line-height: 1;
    letter-spacing: 10px;
    color: var(--headline);
    text-shadow: 0 3px 6px rgba(0,0,0,0.4);
  }
  .sign__call-label {
    position: absolute;
    left: 330px; top: 188px;
    font-family: 'Playball', cursive;
    font-size: 68px;
    color: var(--script);
  }
  .sign__phone {
    position: absolute;
    left: 300px; top: 268px;
    font-family: 'Oswald', sans-serif;
    font-weight: 600;
    font-size: 58px;
    letter-spacing: 2px;
    color: var(--phone);
  }
  .sign__porthole {
    position: absolute;
    right: 28px; top: 18px;
    width: 320px; height: 320px;
    border-radius: 50%;
    border: 12px solid #b9bcc0;
    background: radial-gradient(circle at 60% 45%, #d9a684 0%, #8a6a58 45%, #2a2a30 100%);
    box-shadow: 0 0 0 3px #6f7378;
  }
</style>
</head>
<body>
  <div class="sign">
    <div class="sign__mascot" role="img" aria-label="Cartoon washing machine holding a washing line with hanging clothes"></div>
    <div class="sign__headline">LAUNDROMAT</div>
    <div class="sign__call-label">Free Call</div>
    <div class="sign__phone">1800 555 017</div>
    <div class="sign__porthole" role="img" aria-label="Photo of a woman curled up inside a washing machine drum, seen through the round door"></div>
  </div>
</body>
</html>
```